The Willow Gate: Steady Horizon

Please use the attached images as a reference and as inspiration for this contest. Please note, these images are google searched and belong to someone else.
This project is for our church.
We have a new Sermon Series launching and we want to be able to promote it and manipulate the size of the project via Facebook Cover Art, CD Labels, T-Shirts, Banners, etc.
Requesting a HD 1080 X 920 pixels.
Need an editable PSD file from the winner of the contest.
The title of the project is: Steady Horizon.
The idea behind this project is bringing things in life into focus to help our congregation be intentional about focusing on making positive changes to major areas of life.
When we think of this - we think of a camera brining something into focus to take that perfect shot, or as one of the attached images show blurry images coming into focus.
Keywords that can be used in the design are: Faith, Family, Finances, and Fitness.
Just because it is for a church does NOT mean we need it to look like its for a church. In fact, we desire the design to be compelling to someone who has never stepped foot into a church building. Avoid a "church" look.
Good Luck!
Target Market(s)
Everyone
Industry/Entity Type
House
Requirements
Must have
- Bringing "things" into focus.
- Please read description for more details
Should not have
- A church look

```html
<!DOCTYPE html>
<html lang="en">
<head>
<meta charset="utf-8">
<title>Steady Horizon</title>
<link href="https://fonts.googleapis.com/css2?family=Montserrat:wght@500;600;700&family=Cormorant+Garamond:wght@500&family=Great+Vibes&display=swap" rel="stylesheet">
<style>
  :root {
    --deep-blue: #2a5fd6;
    --mid-blue: #4f86e6;
    --pale-blue: #a9cdf5;
    --haze: #c9dcf4;
    --title-yellow: #f5d90a;
    --title-white: #ffffff;
    --aqua: #36c3e6;
    --faith-blue: #cfe6fb;
  }
  * { margin: 0; padding: 0; box-sizing: border-box; }
  html, body {
    width: 1200px; height: 1022px; overflow: hidden;
    background: var(--deep-blue);
  }
  .canvas {
    position: relative; width: 1200px; height: 1022px; overflow: hidden;
    font-family: 'Montserrat', Arial, sans-serif;
  }
  .backdrop {
    position: absolute; inset: 0;
    background:
      radial-gradient(circle at 8% 6%, rgba(210,240,255,.85) 0 70px, transparent 110px),
      radial-gradient(circle at 95% 12%, rgba(240,245,255,.9) 0 70px, transparent 120px),
      radial-gradient(circle at 47% 28%, rgba(220,170,220,.55) 0 60px, transparent 90px),
      radial-gradient(circle at 62% 60%, rgba(255,200,220,.5) 0 60px, transparent 110px),
      radial-gradient(circle at 70% 78%, rgba(235,240,255,.6) 0 110px, transparent 190px),
      radial-gradient(circle at 38% 62%, rgba(160,220,250,.55) 0 70px, transparent 110px),
      radial-gradient(circle at 6% 58%, rgba(210,150,200,.45) 0 70px, transparent 110px),
      radial-gradient(ellipse at 50% 100%, rgba(210,225,245,.8), transparent 60%),
      linear-gradient(160deg, #6f94d8 0%, var(--mid-blue) 35%, var(--deep-blue) 60%, #5d8fe0 100%);
  }
  .title-kicker {
    position: absolute; left: 195px; top: 382px; width: 805px;
    display: flex; justify-content: space-between;
    color: var(--title-yellow); font-weight: 700; font-size: 38px; line-height: 1;
  }
  .title-main {
    position: absolute; left: 190px; top: 438px; width: 815px;
    display: flex; justify-content: space-between;
    color: var(--title-white); font-weight: 500; font-size: 128px; line-height: 1;
  }
  .title-main .soft { filter: blur(3px); }
  .title-main .softer { filter: blur(5px); }
  .stack {
    position: absolute; display: flex; flex-direction: column; align-items: center;
    line-height: 1;
  }
  .word-church {
    left: 318px; top: 68px; gap: 4px;
    font-family: 'Cormorant Garamond', Georgia, serif; font-size: 38px;
    color: rgba(255,255,255,.85);
  }
  .word-church .blur { filter: blur(3px); opacity: .7; }
  .word-faith {
    left: 1100px; top: 152px; gap: 26px;
    font-weight: 700; font-size: 42px; color: var(--faith-blue); opacity: .85;
    filter: blur(1.5px);
  }
  .word-faith .lead { color: #7fb6f0; filter: blur(0); }
  .word-family {
    left: 190px; top: 578px; gap: 20px;
    font-weight: 500; font-size: 44px; color: var(--title-white);
  }
  .word-family .blur { filter: blur(2px); opacity: .75; }
  .word-health {
    position: absolute; left: 430px; top: 160px; width: 560px;
    display: flex; justify-content: space-between;
    font-weight: 700; font-size: 80px; line-height: 1;
    color: var(--aqua); opacity: .7; filter: blur(3px);
  }
  .word-money {
    position: absolute; left: 432px; top: 600px;
    font-weight: 600; font-size: 110px; line-height: 1;
    color: rgba(255,255,255,.35); filter: blur(2px);
  }
  .word-friends {
    position: absolute; left: 640px; top: 660px;
    font-family: 'Great Vibes', cursive; font-size: 110px; line-height: 1;
    letter-spacing: 14px; color: var(--aqua); opacity: .75; filter: blur(1.5px);
  }
</style>
</head>
<body>
<div class="canvas">
  <div class="backdrop" role="img" aria-label="Soft out-of-focus bokeh lights in blue, aqua and pink tones"></div>

  <div class="stack word-church">
    <span class="blur">C</span><span>H</span><span>U</span><span>R</span><span>C</span><span class="blur">H</span>
  </div>

  <div class="word-health"><span>H</span><span>E</span><span>A</span><span>L</span><span>T</span><span>H</span></div>

  <div class="stack word-faith">
    <span class="lead">F</span><span>A</span><span>I</span><span>T</span><span>H</span>
  </div>

  <h1>
    <div class="title-kicker"><span>S</span><span>T</span><span>E</span><span>A</span><span>D</span><span>Y</span></div>
    <div class="title-main">
      <span class="softer">H</span><span class="soft">O</span><span>R</span><span>I</span><span>Z</span><span class="soft">O</span><span class="softer">N</span>
    </div>
  </h1>

  <div class="stack word-family">
    <span class="blur">A</span><span class="blur">M</span><span class="blur">I</span><span>L</span><span>Y</span>
  </div>

  <div class="word-money">$</div>
  <div class="word-friends">friends</div>
</div>
</body>
</html>
```